Redesign of outdated "Automotive Automation Company"

We are looking to finally update our outdated website with some cutting edge graphics. We want our customers to know we value technology and are cutting edge as far as design. We provide automation solutions for the automotive industry which essentially means we program robots, and sell automation related products.

Current URL

http://lnk.vemrota.com/Qx7pwe
Updates

Project Deadline Extended
Reason: The client portal wasn't working, it's just finally been fixed by Pixel Harbor. I will go through and start reviewing designs.

We are trying to go with the same look and feel on our business cards, line cards, apparel, etc. so we are forming a brand. I have included the current draft of the line card. Please utilize our newest Logo TLV Standardized Logo.jpg http://img.solvarenpics.com/pz3Tm8d.jpg?1 Also we are trying hard to sell the following software / hardware companies so we can put some emphasis on their product. Meridel Controls https://www.meridelcontrols.com/ We make money on selling the software and then on the integration. I think you should tie in this animation. ยท From Shop Chaos to Smooth Output https://media.vorplexclips.com/deliveries/938127a4b51dfe03c7724bde1209f74a615b830c.jpg?image_play_button=true&image_play_button_color=7b796ae0&image_crop_resized=275x155 In this 2-minute video, discover how Quellwave can help run your plant floor. We are Authorized Integrators / Resellers for Tamberly Mechatronics Varnoth Sensorik http://varnoth.com/en/usa/ Meridel Controls https://www.meridelcontrols.com/ Corvane Process Works www.cpwkx.com Halberd Transfer Corp www.halberdtransfer.com Pennwick Machining http://www.pennwickmachining.com/strategic_partners.aspx

Target Market(s)

Large automotive companies looking for automation or robotic programming. So Professional is key.

Industry/Entity Type

Automotive

Font styles to use
Other font styles liked:
• Possible Open Sans or Lato

Colors
0591cc
ceeaf6
fbd4d5
fbf289
fece3e

Requirements
Must have
• Professional Modern Design.

I want a homepage design, and a rough Sales Page... Where numerous products can be listed.
Nice to have
• Maybe an updated logo if possible.

```html
<!DOCTYPE html>
<html lang="en">
<head>
<meta charset="utf-8">
<title>TLV Engineering Solutions</title>
<link rel="stylesheet" href="https://fonts.googleapis.com/css2?family=Arimo:wght@400;700&display=swap">
<style>
:root{
  --pink:#e5195a;
  --blue:#0591cc;
  --yellow:#fece3e;
  --dark:#222222;
  --ink:#444444;
  --grey:#777777;
  --green:#8dc63f;
  --white:#ffffff;
}
*{margin:0;padding:0;box-sizing:border-box}
html,body{width:1200px;height:2497px;overflow:hidden}
body{position:relative;background:var(--white);font-family:"Arimo",Arial,sans-serif;color:var(--ink)}
.abs{position:absolute}

/* header */
.header{left:0;top:0;width:1200px;height:141px;background:var(--white);box-shadow:0 2px 4px rgba(0,0,0,.12);z-index:2}
.brand{left:92px;top:46px;display:flex;align-items:center;gap:12px}
.brand-mark{width:40px;height:40px;border-radius:50%;background:var(--pink)}
.brand-name{font-size:22px;font-weight:700;color:var(--ink)}
.call{left:965px;top:12px;display:flex;gap:10px;align-items:flex-start}
.call-label{font-size:14px;color:#333;line-height:19px}
.call-number{font-size:14px;color:var(--pink);line-height:19px}
.nav{left:672px;top:58px;width:435px;height:47px;background:var(--pink);border-radius:6px;display:flex;box-shadow:0 2px 3px rgba(0,0,0,.25)}
.nav a{flex:1;display:flex;align-items:center;justify-content:center;gap:6px;color:var(--white);font-size:13.5px;font-weight:700;text-decoration:none;border-left:1px solid rgba(255,255,255,.45)}
.nav a:first-child{border-left:0;flex:1.45;color:#7a1030}

/* hero */
.hero{left:0;top:141px;width:1200px;height:445px;background:radial-gradient(ellipse at 40% 50%,#f4f6f9 0%,#dfe4ea 60%,#c9d0d9 100%)}
.hero-title{left:133px;top:252px;font-size:36px;color:var(--pink);font-variant:small-caps;letter-spacing:.5px}
.hero-sub{left:133px;top:302px;font-size:17px;color:#333;font-variant:small-caps}
.hero-arrow{top:343px;width:47px;height:47px;border-radius:50%;background:var(--pink);display:flex;align-items:center;justify-content:center;box-shadow:0 2px 3px rgba(0,0,0,.3)}
.hero-visual{left:790px;top:150px;width:317px;height:433px;background:linear-gradient(160deg,#8e9db8 0%,#4f5f7e 55%,#b9c2d0 100%);border-radius:40px 40px 10px 10px;opacity:.85}

/* call to action band */
.cta{left:0;top:586px;width:1200px;height:86px;background:var(--blue)}
.cta-text{left:92px;top:612px;font-size:21px;color:var(--white);font-variant:small-caps;letter-spacing:.4px}
.btn{top:609px;height:40px;display:flex;align-items:center;justify-content:center;font-size:13.5px;font-weight:700;color:#333}
.btn-quote{left:795px;width:137px;background:var(--yellow)}
.btn-overview{left:945px;width:157px;border:3px solid #2d3b46;color:#1f2b33}

/* overview */
.section-title{left:0;width:1200px;text-align:center;font-size:42px;font-weight:700;color:var(--ink)}
.rule{left:316px;top:749px;width:571px;height:1px;background:#aaa}
.service{width:320px;text-align:center}
.service svg{display:block;margin:0 auto}
.service h3{margin-top:22px;font-size:13px;font-weight:700;color:#222;letter-spacing:.3px}
.service p{width:276px;margin:10px auto 0;font-size:12.5px;line-height:16.6px;color:var(--grey)}

/* yellow section */
.premier{left:0;top:1273px;width:1200px;height:463px;background:var(--yellow)}
.premier-title{left:0;top:1294px;width:1200px;text-align:center;font-size:21px;font-weight:700;color:#222}
.premier-sub{left:0;top:1325px;width:1200px;text-align:center;font-size:17px;color:#111}
.premier-copy{left:92px;top:1350px;width:1015px;text-align:center;font-size:13.5px;line-height:22.5px;color:#b87a3a}
.team-card{top:1454px;width:285px}
.team-photo{width:285px;height:188px;background:linear-gradient(180deg,#e9edf1 0%,#c9ccd2 45%,#5a6270 100%);position:relative;overflow:hidden}
.team-photo::before{content:"";position:absolute;left:0;top:0;border-top:44px solid #222;border-right:44px solid transparent}
.team-plus{position:absolute;left:7px;top:2px;color:#fff;font-size:18px;font-weight:700}
.team-caption{margin-top:8px;font-size:13.5px;color:#222}

/* specialties */
.specialties{left:0;top:1736px;width:1200px;height:502px;background:radial-gradient(ellipse at 45% 55%,#4a4a4a 0%,#2b2b2b 55%,#1c1c1c 100%)}
.spec-title{left:0;top:1768px;width:1200px;text-align:center;font-size:25px;font-weight:700;color:var(--green)}
.spec-list{list-style:none;top:1840px}
.spec-list li{height:35.6px;display:flex;align-items:center;gap:10px;font-size:17.5px;color:var(--white)}

/* footer */
.footer-rule{left:0;top:2238px;width:1200px;height:5px;background:var(--yellow)}
.footer{left:0;top:2243px;width:1200px;height:222px;background:var(--dark)}
.foot-head{font-size:14px;font-weight:700;color:var(--yellow)}
.foot-col{list-style:none}
.foot-col li{font-size:11px;font-weight:700;color:var(--white);height:20px;line-height:20px}
.accepted{left:837px;top:2285px;font-size:13.5px;font-weight:700;color:var(--white)}
.card{top:2321px;height:40px;background:#f2f2f2;border:1px solid #999}
.follow{left:837px;top:2394px;display:flex;align-items:center;gap:12px;font-size:13.5px;font-weight:700;color:var(--white)}
.social{width:12px;height:12px;border-radius:50%;background:var(--white)}
.copyright{left:0;top:2465px;width:1200px;height:32px;background:var(--pink);color:var(--white);font-size:12.5px;display:flex;align-items:center;justify-content:center}
.copyright span{font-variant:small-caps}
</style>
</head>
<body>

<header class="abs header">
  <div class="abs brand"><span class="brand-mark"></span><span class="brand-name">TLV Engineering Solutions</span></div>
  <div class="abs call">
    <svg width="14" height="26" viewBox="0 0 14 26"><rect x="1" y="1" width="12" height="24" rx="2" fill="none" stroke="#222" stroke-width="2"/><rect x="3" y="4" width="8" height="15" fill="#222"/></svg>
    <div><div class="call-label">GIVE US A CALL:</div><div class="call-number">+1800 555 014</div></div>
  </div>
  <nav class="abs nav">
    <a href="#"><svg width="14" height="12" viewBox="0 0 14 12"><path d="M7 0 14 6H12V12H8.5V8H5.5V12H2V6H0Z" fill="#7a1030"/></svg>Home Page</a>
    <a href="#">Services</a>
    <a href="#">Contact</a>
    <a href="#">About</a>
  </nav>
</header>

<section class="abs hero"></section>
<div class="abs hero-title">TLV Engineering Solutions</div>
<div class="abs hero-sub">Your Premier Automation Consulting &amp; Systems Integration choice!</div>
<div class="abs hero-arrow" style="left:132px"><svg width="14" height="16" viewBox="0 0 14 16"><path d="M11 1 3 8l8 7" fill="none" stroke="#fff" stroke-width="3"/></svg></div>
<div class="abs hero-arrow" style="left:195px"><svg width="14" height="16" viewBox="0 0 14 16"><path d="M3 1l8 7-8 7" fill="none" stroke="#fff" stroke-width="3"/></svg></div>
<div class="abs hero-visual" role="img" aria-label="Two humanoid industrial robots standing side by side"></div>

<section class="abs cta"></section>
<div class="abs cta-text">Mi eget. Ut vitae ac, nec suscipit. Ut rutrum et. Sodales pellentesque.</div>
<div class="abs btn btn-quote">GET A QUOTE</div>
<div class="abs btn btn-overview">OVERVIEW</div>

<h2 class="abs section-title" style="top:694px">OVERVIEW</h2>
<div class="abs rule"></div>

<div class="abs service" style="left:70px;top:792px">
  <svg width="74" height="74" viewBox="0 0 74 74"><circle cx="37" cy="37" r="30" fill="#333" stroke="#333" stroke-width="10" stroke-dasharray="6 5"/><circle cx="37" cy="37" r="20" fill="var(--pink)"/><circle cx="37" cy="37" r="12" fill="#fff"/></svg>
  <h3>APPLICATIONS ENGINEERING</h3>
  <p>Provide electrical and mechanical expertise to solve automation specific application problems by utilizing best known industry practices.</p>
</div>
<div class="abs service" style="left:439px;top:792px">
  <svg width="74" height="74" viewBox="0 0 74 74"><circle cx="37" cy="37" r="27" fill="#333" stroke="#333" stroke-width="8" stroke-dasharray="6 5"/><circle cx="37" cy="37" r="19" fill="var(--pink)"/><g fill="#333"><circle cx="30" cy="37" r="4"/><circle cx="44" cy="30" r="4"/><circle cx="44" cy="44" r="4"/></g><path d="M30 37 44 30M30 37 44 44" stroke="#333" stroke-width="2"/></svg>
  <h3>CONTROLS ENGINEERING</h3>
  <p>Design and implement control programs on PLC's, SCADA, HMI's, Vision Systems, Robots and Motion Controls specific to each application and project requirements with the ability to interface to a database.</p>
</div>
<div class="abs service" style="left:810px;top:792px">
  <svg width="74" height="74" viewBox="0 0 74 74"><circle cx="37" cy="37" r="27" fill="#333" stroke="#333" stroke-width="8" stroke-dasharray="6 5"/><circle cx="37" cy="37" r="19" fill="var(--pink)"/><g fill="#333"><circle cx="30" cy="37" r="4"/><circle cx="44" cy="30" r="4"/><circle cx="44" cy="44" r="4"/></g><path d="M30 37 44 30M30 37 44 44" stroke="#333" stroke-width="2"/></svg>
  <h3>DESIGN ENGINEERING</h3>
  <p>Provide electro-mechanical designs for machine downtime improvements and cost reductions. Perform sizing calculations for motion control and fluid power applications.</p>
</div>
<div class="abs service" style="left:70px;top:1028px">
  <svg width="74" height="74" viewBox="0 0 74 74"><circle cx="37" cy="37" r="27" fill="#333" stroke="#333" stroke-width="8" stroke-dasharray="6 5"/><circle cx="37" cy="37" r="19" fill="var(--pink)"/><g fill="#333"><circle cx="30" cy="37" r="4"/><circle cx="44" cy="30" r="4"/><circle cx="44" cy="44" r="4"/></g><path d="M30 37 44 30M30 37 44 44" stroke="#333" stroke-width="2"/></svg>
  <h3>DESIGN SPECIFICATION</h3>
  <p>Develop controls andmechanicalspecificationsfor machines to beused when purchasing equipment. Collaborate with the systems integrator /machine OEM to ensure adherence to machine specifications.</p>
</div>
<div class="abs service" style="left:439px;top:1028px">
  <svg width="74" height="74" viewBox="0 0 74 74"><circle cx="37" cy="37" r="27" fill="#333" stroke="#333" stroke-width="8" stroke-dasharray="6 5"/><circle cx="37" cy="37" r="19" fill="var(--pink)"/><g fill="#333"><circle cx="30" cy="37" r="4"/><circle cx="44" cy="30" r="4"/><circle cx="44" cy="44" r="4"/></g><path d="M30 37 44 30M30 37 44 44" stroke="#333" stroke-width="2"/></svg>
  <h3>ELECTRICAL ENGINEERING</h3>
  <p>Design and develop electrical schematics with DraftaCAD 2014 to be used in constructing control solutions for automated equipment.</p>
</div>
<div class="abs service" style="left:810px;top:1028px">
  <svg width="74" height="74" viewBox="0 0 74 74"><circle cx="37" cy="37" r="27" fill="#333" stroke="#333" stroke-width="8" stroke-dasharray="6 5"/><circle cx="37" cy="37" r="19" fill="var(--pink)"/><g fill="#333"><circle cx="30" cy="37" r="4"/><circle cx="44" cy="30" r="4"/><circle cx="44" cy="44" r="4"/></g><path d="M30 37 44 30M30 37 44 44" stroke="#333" stroke-width="2"/></svg>
  <h3>FIELD INSTALLATION</h3>
  <p>Perform retrofits,upgrade sand online be a programming changes to production settings, including model year changeovers, errorproofing, bar code data parsing and KAIZEN project implementations...</p>
</div>

<section class="abs premier"></section>
<h2 class="abs premier-title">YOUR PREMIER AUTOMATION CONSULTING &amp; SYSTEMS INTEGRATION CHOICE!</h2>
<div class="abs premier-sub">HELPING YOUR BUSINESS OPTIMIZE ITS AUTOMATION....</div>
<p class="abs premier-copy">Industrial Automation is constantly evolving with ever-changing technological breakthroughs. For companies to remain competitive, they need to be more nimble than ever implementing productivity and manufacturing innovations. But identifying and implementing the right Automation, Robotics and Industrial Controls is never easy. That's where our team of experts comes in to play bringing our proven experience to the table.</p>

<div class="abs team-card" style="left:101px"><div class="team-photo" role="img" aria-label="Group of business professionals standing together"><span class="team-plus">+</span></div><div class="team-caption">GET TO KNOW OUR TEAM APPROACH</div></div>
<div class="abs team-card" style="left:459px"><div class="team-photo" role="img" aria-label="Group of business professionals standing together"><span class="team-plus">+</span></div><div class="team-caption">THIS WAY TO AUTOMATION SUCCESS</div></div>
<div class="abs team-card" style="left:814px"><div class="team-photo" role="img" aria-label="Group of business professionals standing together"><span class="team-plus">+</span></div><div class="team-caption">BRING GREAT IDEAS TO YOUR BUSINESS</div></div>

<section class="abs specialties" role="img" aria-label="Dim background scene of a child playing with a small robot"></section>
<h2 class="abs spec-title">SPECIALIZING IN THE FOLLOWING AREAS</h2>
<ul class="abs spec-list" style="left:103px">
  <li><svg width="16" height="14" viewBox="0 0 16 14"><path d="M1 7l5 5L15 1" fill="none" stroke="#8dc63f" stroke-width="3"/></svg>2D and 3D Capabilities</li>
  <li><svg width="16" height="14" viewBox="0 0 16 14"><path d="M1 7l5 5L15 1" fill="none" stroke="#8dc63f" stroke-width="3"/></svg>Consulting</li>
  <li><svg width="16" height="14" viewBox="0 0 16 14"><path d="M1 7l5 5L15 1" fill="none" stroke="#8dc63f" stroke-width="3"/></svg>Controls Engineering</li>
  <li><svg width="16" height="14" viewBox="0 0 16 14"><path d="M1 7l5 5L15 1" fill="none" stroke="#8dc63f" stroke-width="3"/></svg>Applications</li>
  <li><svg width="16" height="14" viewBox="0 0 16 14"><path d="M1 7l5 5L15 1" fill="none" stroke="#8dc63f" stroke-width="3"/></svg>Automation Product Sales</li>
  <li><svg width="16" height="14" viewBox="0 0 16 14"><path d="M1 7l5 5L15 1" fill="none" stroke="#8dc63f" stroke-width="3"/></svg>Data Acquisition</li>
  <li><svg width="16" height="14" viewBox="0 0 16 14"><path d="M1 7l5 5L15 1" fill="none" stroke="#8dc63f" stroke-width="3"/></svg>Contract Engineering /Techs</li>
  <li><svg width="16" height="14" viewBox="0 0 16 14"><path d="M1 7l5 5L15 1" fill="none" stroke="#8dc63f" stroke-width="3"/></svg>Custom Automated Equipment</li>
</ul>
<ul class="abs spec-list" style="left:494px">
  <li><svg width="16" height="14" viewBox="0 0 16 14"><path d="M1 7l5 5L15 1" fill="none" stroke="#8dc63f" stroke-width="3"/></svg>2D and 3D Capabilities</li>
  <li><svg width="16" height="14" viewBox="0 0 16 14"><path d="M1 7l5 5L15 1" fill="none" stroke="#8dc63f" stroke-width="3"/></svg>Consulting</li>
  <li><svg width="16" height="14" viewBox="0 0 16 14"><path d="M1 7l5 5L15 1" fill="none" stroke="#8dc63f" stroke-width="3"/></svg>Controls Engineering</li>
  <li><svg width="16" height="14" viewBox="0 0 16 14"><path d="M1 7l5 5L15 1" fill="none" stroke="#8dc63f" stroke-width="3"/></svg>Applications</li>
  <li><svg width="16" height="14" viewBox="0 0 16 14"><path d="M1 7l5 5L15 1" fill="none" stroke="#8dc63f" stroke-width="3"/></svg>Automation Product Sales</li>
  <li><svg width="16" height="14" viewBox="0 0 16 14"><path d="M1 7l5 5L15 1" fill="none" stroke="#8dc63f" stroke-width="3"/></svg>Data Acquisition</li>
  <li><svg width="16" height="14" viewBox="0 0 16 14"><path d="M1 7l5 5L15 1" fill="none" stroke="#8dc63f" stroke-width="3"/></svg>Contract Engineering /Techs</li>
  <li><svg width="16" height="14" viewBox="0 0 16 14"><path d="M1 7l5 5L15 1" fill="none" stroke="#8dc63f" stroke-width="3"/></svg>Custom Automated Equipment</li>
</ul>
<ul class="abs spec-list" style="left:845px">
  <li><svg width="16" height="14" viewBox="0 0 16 14"><path d="M1 7l5 5L15 1" fill="none" stroke="#8dc63f" stroke-width="3"/></svg>2D and 3D Capabilities</li>
  <li><svg width="16" height="14" viewBox="0 0 16 14"><path d="M1 7l5 5L15 1" fill="none" stroke="#8dc63f" stroke-width="3"/></svg>Consulting</li>
  <li><svg width="16" height="14" viewBox="0 0 16 14"><path d="M1 7l5 5L15 1" fill="none" stroke="#8dc63f" stroke-width="3"/></svg>Controls Engineering</li>
  <li><svg width="16" height="14" viewBox="0 0 16 14"><path d="M1 7l5 5L15 1" fill="none" stroke="#8dc63f" stroke-width="3"/></svg>Applications</li>
  <li><svg width="16" height="14" viewBox="0 0 16 14"><path d="M1 7l5 5L15 1" fill="none" stroke="#8dc63f" stroke-width="3"/></svg>Automation Product Sales</li>
  <li><svg width="16" height="14" viewBox="0 0 16 14"><path d="M1 7l5 5L15 1" fill="none" stroke="#8dc63f" stroke-width="3"/></svg>Data Acquisition</li>
  <li><svg width="16" height="14" viewBox="0 0 16 14"><path d="M1 7l5 5L15 1" fill="none" stroke="#8dc63f" stroke-width="3"/></svg>Contract Engineering /Techs</li>
  <li><svg width="16" height="14" viewBox="0 0 16 14"><path d="M1 7l5 5L15 1" fill="none" stroke="#8dc63f" stroke-width="3"/></svg>Custom Automated Equipment</li>
</ul>

<div class="abs footer-rule"></div>
<footer class="abs footer"></footer>
<div class="abs foot-head" style="left:93px;top:2261px">AREAS OF EXPERTISE</div>
<div class="abs foot-head" style="left:93px;top:2284px">HMI'S</div>
<ul class="abs foot-col" style="left:95px;top:2315px"><li>Ashford Brill</li><li>Mizuharu</li><li>Ashford Brill</li><li>Mizuharu</li><li>Ashford Brill</li><li>Mizuharu</li></ul>
<ul class="abs foot-col" style="left:186px;top:2315px"><li>Ashford Brill</li><li>Mizuharu</li><li>Ashford Brill</li><li>Mizuharu</li><li>Ashford Brill</li><li>Mizuharu</li></ul>
<div class="abs foot-head" style="left:324px;top:2288px;font-weight:400">MOTION CONTROL</div>
<ul class="abs foot-col" style="left:324px;top:2315px"><li>Ashford Brill</li><li>Mizuharu</li><li>Ashford Brill</li><li>Mizuharu</li><li>Ashford Brill</li><li>Mizuharu</li></ul>
<div class="abs foot-head" style="left:517px;top:2288px;font-weight:400">ROBOTICS</div>
<ul class="abs foot-col" style="left:517px;top:2315px"><li>Ashford Brill</li><li>Mizuharu</li><li>Ashford Brill</li><li>Mizuharu</li><li>Ashford Brill</li><li>Mizuharu</li></ul>
<div class="abs foot-head" style="left:666px;top:2288px;font-weight:400">VISION</div>
<ul class="abs foot-col" style="left:666px;top:2315px"><li>Ashford Brill</li><li>Mizuharu</li><li>Ashford Brill</li><li>Mizuharu</li><li>Ashford Brill</li><li>Mizuharu</li></ul>

<div class="abs accepted">We proudly accepted</div>
<div class="abs card" style="left:834px;width:58px"></div>
<div class="abs card" style="left:895px;width:62px"></div>
<div class="abs card" style="left:960px;width:60px"></div>
<div class="abs card" style="left:1024px;width:63px"></div>
<div class="abs follow">Follow Us:<span class="social"></span><span class="social"></span><span class="social"></span></div>

<div class="abs copyright">2014 Copyright-<span>TLV Engineering Solutions</span>. All rights reseverd</div>

</body>
</html>
```